SPARK - and the compass of quiet days

I´m writing a book about CHANGE and the skills leaders needs to embody the transformation from being amanager to become leaders.
The title of the book in Icelandic is the same as the name of the project (which I want to be used on the designes is:) HAFALDAN
(with the subtitle:) og listin að hlusta

Change is not controlled or managed – Leading effective change is an art form which is one of the big reasons for why 70% of changes within companies fail. The main reason however, is that managers are tasked with managing and directing them. The art form of change is to put it in the hands of leaders who possess the emotional intelligence that is needed – all their other advantages intact – to lead change all the way.

The big problem when it comes to change is that there are too many managers and too few leaders within companies – leaders who possess emotional intelligence which is the most important skill a leader embodies to empower change. A leader has what it takes to empower followership.

A manager tends to push and control, make decisions that he presupposes others to implement the way he expects. An emotionally competent leader leads by example and enhances followership on that journey because of the trust and respect he has earned.

In few words: SOFT SKILLS ARE THE NEW HARD SKILLS!

```html
<!DOCTYPE html>
<html lang="is">
<head>
<meta charset="utf-8">
<title>HAFALDAN – og listin að hlusta</title>
<link href="https://fonts.googleapis.com/css2?family=Montserrat:wght@400;500;700&display=swap" rel="stylesheet">
<style>
  :root {
    --backdrop: #929292;
    --paper: #ffffff;
    --band-orange: #f59835;
    --title-red: #ef5230;
    --text-maroon: #751414;
    --art-teal: #76aeaa;
    --art-orange: #f59835;
  }
  html, body {
    margin: 0;
    padding: 0;
    width: 1200px;
    height: 1200px;
    overflow: hidden;
    background: var(--backdrop);
    font-family: "Montserrat", Arial, sans-serif;
  }
  .book-cover {
    position: absolute;
    left: 129px;
    top: 129px;
    width: 941px;
    height: 941px;
    background: var(--paper);
    box-shadow: 10px 14px 28px rgba(0, 0, 0, 0.35);
    overflow: hidden;
  }
  .spine-band {
    position: absolute;
    top: 0;
    left: 0;
    width: 134px;
    height: 100%;
  }
  .cover-title {
    position: absolute;
    left: 170px;
    width: 725px;
    top: 80px;
    margin: 0;
    text-align: center;
    font-weight: 700;
    font-size: 108px;
    line-height: 1;
    color: var(--title-red);
    letter-spacing: 1px;
  }
  .cover-subtitle {
    position: absolute;
    left: 170px;
    width: 725px;
    top: 193px;
    margin: 0;
    text-align: center;
    font-weight: 400;
    font-size: 41px;
    line-height: 1.2;
    color: var(--text-maroon);
  }
  .cover-illustration {
    position: absolute;
    left: 285px;
    top: 341px;
    width: 518px;
    height: 345px;
    border-radius: 24px;
    background: linear-gradient(35deg, rgba(118, 174, 170, 0.55) 0%, rgba(118, 174, 170, 0.45) 55%, rgba(245, 152, 53, 0.6) 100%);
  }
  .cover-author {
    position: absolute;
    left: 170px;
    width: 725px;
    top: 812px;
    margin: 0;
    text-align: center;
    font-weight: 500;
    font-size: 37px;
    letter-spacing: 8px;
    color: var(--text-maroon);
  }
</style>
</head>
<body>
  <div class="book-cover">
    <svg class="spine-band" viewBox="0 0 134 941" aria-hidden="true">
      <rect x="0" y="0" width="93" height="941" fill="var(--band-orange)"/>
      <rect x="101" y="0" width="19" height="941" fill="var(--band-orange)"/>
      <rect x="127" y="0" width="7" height="941" fill="var(--band-orange)"/>
    </svg>
    <h1 class="cover-title">HAFALDAN</h1>
    <p class="cover-subtitle">og listin að hlusta</p>
    <div class="cover-illustration" role="img" aria-label="Illustration of a small figure climbing a rising path of rounded teal stepping stones from a small red square toward a large orange shape"></div>
    <p class="cover-author">AUTHOR NAME</p>
  </div>
</body>
</html>
```